New Infographic Design Project

I need a 1 page Infographic that explains our Quillstone Prism offer.

Can you use the following content in the attached document to create a 1 page infographic. The image in the bottom of the document is one of our competitors who is offering the same thing, this image is only provided for inspiration and ideas as we need ours to be based on the content of the document and aligned with the Corvenly Brand

```html
<!DOCTYPE html>
<html lang="en">
<head>
<meta charset="utf-8">
<title>Data Ready, AI Ready in 6 Weeks – Corvenly</title>
<link rel="stylesheet" href="https://fonts.googleapis.com/css2?family=Poppins:wght@300;400;500;600;700;800&family=Orbitron:wght@800&display=swap">
<style>
  :root{
    --mat:#a9a9a9;
    --maroon:#7d0007;
    --maroon-deep:#5e0005;
    --red:#e8262f;
    --white:#ffffff;
    --ink:#141414;
    --frame-grey:#c9c9c9;
  }
  *{margin:0;padding:0;box-sizing:border-box}
  html,body{width:908px;height:1200px;overflow:hidden}
  body{background:var(--mat);font-family:"Poppins",sans-serif;position:relative}

  .sheet{
    position:absolute;left:144px;top:161px;width:621px;height:878px;overflow:hidden;
    background:
      radial-gradient(ellipse 70% 22% at 50% 84%, rgba(238,42,51,.55), rgba(238,42,51,0) 70%),
      linear-gradient(180deg,var(--maroon) 0%,#8a050c 55%,#b0121a 80%,#c4161f 100%);
    color:var(--white);
  }
  .network-texture{position:absolute;left:0;top:700px;width:621px;height:120px;
    background:radial-gradient(ellipse at 50% 60%,rgba(255,120,120,.18),rgba(255,120,120,0) 70%)}
  .abs{position:absolute}

  .headline-top{left:0;width:621px;top:22px;font-size:45px;font-weight:400;line-height:1;letter-spacing:-.5px;text-align:center}
  .headline-main{left:0;width:621px;top:60px;font-size:92px;font-weight:700;line-height:1;letter-spacing:-3px;color:var(--red);text-align:center}
  .tagline{left:0;width:621px;top:149px;font-size:14.5px;font-weight:600;text-align:center;letter-spacing:.1px}
  .intro{left:0;width:621px;top:170px;font-size:7.9px;font-weight:300;line-height:12px;text-align:center;white-space:nowrap;letter-spacing:-.05px}

  .edge-frame{left:19px;top:221px;width:582px;height:172px;border:1.5px solid rgba(255,255,255,.45);border-radius:22px}
  .edge-panel{left:23px;top:227px;width:576px;height:156px;background:var(--white);border-radius:18px}
  .edge-pill{left:207px;top:213px;width:206px;height:28px;background:var(--red);border-radius:14px;
    border-bottom:2px solid var(--maroon-deep);font-size:15.5px;font-weight:700;line-height:26px;text-align:center}
  .edge-divider{top:247px;width:1px;height:126px;background:#d6d6d6}
  .edge-item{width:170px;color:var(--ink);text-align:center;white-space:nowrap}
  .edge-icon{position:absolute;top:250px;width:44px;height:42px}
  .edge-title{top:301px;font-size:8.8px;font-weight:600;line-height:11.5px}
  .edge-text{top:328px;font-size:8.3px;line-height:12px}

  .timeline-panel{left:19px;top:405px;width:582px;height:313px;background:var(--white);border-radius:40px 0 40px 0}
  .timeline-heading{left:0;width:621px;top:408px;font-size:22px;font-weight:700;color:var(--red);text-align:center}
  .timeline-track{position:absolute;left:0;top:0}
  .week{width:200px;text-align:center;color:var(--ink);white-space:nowrap}
  .week-label{font-family:"Orbitron",sans-serif;font-weight:800;font-size:18px;line-height:1;letter-spacing:.5px}
  .week-phase{font-size:9px;color:var(--red);line-height:12px;margin-top:4px}
  .week-detail{width:200px;text-align:center;font-size:8.8px;line-height:12.8px;color:var(--ink);white-space:nowrap}

  .extra-title{left:0;width:621px;top:727px;font-size:18px;font-weight:700;text-align:center;
    text-shadow:0 0 8px rgba(255,90,90,.8)}
  .bottom-band{left:0;top:0}
  .extra-card{top:765px;width:139px;height:92px;background:var(--red);border:1px solid rgba(255,255,255,.75);
    border-radius:12px 2px 20px 2px;text-align:center;padding-top:14px;white-space:nowrap}
  .extra-card h3{font-size:8.8px;font-weight:700;line-height:11.5px}
  .extra-card p{font-size:7.6px;font-weight:300;line-height:11.4px;margin-top:3px;letter-spacing:-.05px}
  .extra-badge{position:absolute;top:747px;width:30px;height:30px}
</style>
</head>
<body>
<main class="sheet">
  <div class="network-texture" role="img" aria-label="Glowing red data network background"></div>

  <h1>
    <span class="abs headline-top">DATA READY, AI READY</span>
    <span class="abs headline-main">IN 6 WEEKS</span>
  </h1>
  <h2 class="abs tagline">YOUR LONG-TERM STRATEGIC DATA PARTNER</h2>
  <p class="abs intro">We start with a Business Data Assessment or Prism Deployment Assessment to pinpoint the highest-value use cases,<br>the biggest data risks, and the fastest path to impact. We stand up a governed Quillstone Prism foundation using repeatable<br>ingestion, validation, and common data model patterns, so your reporting scales cleanly and your AI initiatives provide business value.</p>

  <div class="abs edge-frame"></div>
  <div class="abs edge-panel"></div>
  <div class="abs edge-pill">THE CORVENLY EDGE</div>
  <div class="abs edge-divider" style="left:162px"></div>
  <div class="abs edge-divider" style="left:333px"></div>
  <div class="abs edge-divider" style="left:494px"></div>

  <svg class="edge-icon" style="left:62px" viewBox="0 0 44 42" fill="none" stroke="#e8262f" stroke-width="1.8" stroke-linejoin="round">
    <path d="M12 8h28v20H12z M12 8l4-6h20l4 6 M22 2v10l4-2 4 2V2"/>
    <circle cx="11" cy="30" r="8" fill="#fff"/><circle cx="11" cy="30" r="5"/>
  </svg>
  <svg class="edge-icon" style="left:223px" viewBox="0 0 44 42" fill="none" stroke="#e8262f" stroke-width="1.8">
    <ellipse cx="18" cy="7" rx="15" ry="5"/><path d="M3 7v24c0 3 7 5 15 5 M33 7v12 M3 15c0 3 7 5 15 5s15-2 15-5 M3 23c0 3 7 5 13 5"/>
    <circle cx="32" cy="31" r="8"/><path d="M26 37l12-12"/>
  </svg>
  <svg class="edge-icon" style="left:386px" viewBox="0 0 44 42" fill="none" stroke="#e8262f" stroke-width="1.7" stroke-linejoin="round">
    <path d="M18 2v6 M18 2h6v3h-6 M4 16l14-8 14 8z M6 16v16 M12 19v13 M18 19v13 M24 19v13 M2 32h26v5H2z"/>
    <circle cx="34" cy="31" r="6"/><path d="M31 31l2 2 4-4"/>
  </svg>
  <svg class="edge-icon" style="left:530px" viewBox="0 0 44 42" fill="none" stroke="#e8262f" stroke-width="1.8">
    <circle cx="22" cy="21" r="13"/><circle cx="22" cy="21" r="7"/>
    <path d="M22 3v5 M22 34v5 M4 21h5 M35 21h5 M9 8l4 4 M31 30l4 4 M35 8l-4 4 M9 34l4-4"/>
  </svg>

  <div class="abs edge-item edge-title" style="left:-1px">QUALITY-FIRST<br>DELIVERY</div>
  <div class="abs edge-item edge-text" style="left:-1px">Automated validation,<br>data tests, and “quality<br>gates” that stop bad data<br>upstream.</div>
  <div class="abs edge-item edge-title" style="left:160px">DATA PRODUCTS,<br>NOT DATASETS</div>
  <div class="abs edge-item edge-text" style="left:160px">Clear ownership, SLAs, versioning,<br>and reusable, consumable outputs<br>aligned to high impact business<br>outcomes.</div>
  <div class="abs edge-item edge-title" style="left:323px">GOVERNANCE THAT<br>DOESN'T SLOW YOU DOWN</div>
  <div class="abs edge-item edge-text" style="left:323px">Security, access,<br>lineage, and<br>auditability built in<br>from day one.</div>
  <div class="abs edge-item edge-title" style="left:467px">OPERATE<br>SEAMLESSLY</div>
  <div class="abs edge-item edge-text" style="left:467px">CI/CD, monitoring,<br>and cost controls<br>so the platform<br>stays healthy.</div>

  <div class="abs timeline-panel"></div>
  <h2 class="abs timeline-heading">6 WEEK TIME TO VALUE</h2>
  <svg class="timeline-track" width="621" height="720" viewBox="0 0 621 720">
    <polygon points="46,484 590,484 576,636 32,636" fill="none" stroke="var(--frame-grey)" stroke-width="4"/>
    <polygon points="47,486 587,486 573,633 34,633" fill="none" stroke="var(--red)" stroke-width="1.8"/>
    <g fill="var(--red)">
      <circle cx="136" cy="486" r="6"/><circle cx="306" cy="486" r="6"/><circle cx="483" cy="486" r="6"/>
      <circle cx="136" cy="633" r="6"/><circle cx="306" cy="633" r="6"/><circle cx="483" cy="633" r="6"/>
    </g>
  </svg>

  <div class="abs week" style="left:36px;top:443px"><div class="week-label">WEEK 1</div><div class="week-phase">Envision &amp; Assess</div></div>
  <div class="abs week" style="left:206px;top:443px"><div class="week-label">WEEK 2</div><div class="week-phase">Architecture &amp; governance design</div></div>
  <div class="abs week" style="left:383px;top:443px"><div class="week-label">WEEK 3</div><div class="week-phase">Prism foundation deployed</div></div>
  <div class="abs week-detail" style="left:36px;top:496px">Use case shortlist and priority<br>based on highest business<br>impact, current-state review,<br>data risk &amp; compliance priorities,<br>target operating model.</div>
  <div class="abs week-detail" style="left:206px;top:496px">Landing zone decisions,<br>security and access model,<br>patterns/standards, delivery<br>plan and success metrics.</div>
  <div class="abs week-detail" style="left:383px;top:496px">Workspaces and<br>environments, automation &amp; CI/CD,<br>onboarding playbooks, baseline<br>policies/guardrails.</div>

  <div class="abs week" style="left:36px;top:588px"><div class="week-label">WEEK 4</div><div class="week-phase">Data ingestion + validation framework</div></div>
  <div class="abs week" style="left:206px;top:588px"><div class="week-label">WEEK 5</div><div class="week-phase">Scalable common data model</div></div>
  <div class="abs week" style="left:383px;top:588px"><div class="week-label">WEEK 6</div><div class="week-phase">Business outcomes + AI-ready capability</div></div>
  <div class="abs week-detail" style="left:36px;top:641px">Reusable ingestion patterns,<br>automated validation, data<br>contracts/SLAs, observability<br>signals and alerting.</div>
  <div class="abs week-detail" style="left:206px;top:641px">Domain model, master entities,<br>curated layer, semantic<br>modelling patterns that support<br>Lumenboard at scale.</div>
  <div class="abs week-detail" style="left:383px;top:641px">Executive dashboards and priority<br>reports, performance optimisation,<br>hypercare and handover, AI readiness<br>check and pilot plan (predictive<br>analytics and/or secure enterprise LLM).</div>

  <h2 class="abs extra-title">EXTRA EDGE:</h2>
  <svg class="abs bottom-band" width="621" height="878" viewBox="0 0 621 878">
    <path d="M0 878V842Q0 812 30 812H591Q621 812 621 842V878Z" fill="var(--white)"/>
  </svg>

  <div class="abs extra-card" style="left:19px"><h3>“AI-ready data”<br>guarantee</h3><p>Every priority dataset ships with<br>validation rules, ownership,<br>lineage, and freshness SLAs<br>before it can power AI.</p></div>
  <div class="abs extra-card" style="left:167px"><h3>Cost-to-serve<br>transparency</h3><p>Show business owners what<br>each product/report costs to<br>run and optimise it continuously.</p></div>
  <div class="abs extra-card" style="left:315px"><h3>Change-proof<br>pipelines</h3><p>Data contracts + automated<br>tests reduce breakages from<br>upstream schema changes.</p></div>
  <div class="abs extra-card" style="left:463px"><h3>Governed<br>self-serve</h3><p>Catalog + certified datasets<br>so teams move faster<br>without creating data chaos.</p></div>

  <svg class="extra-badge" style="left:74px" viewBox="0 0 30 30"><circle cx="15" cy="15" r="14" fill="#fff"/><circle cx="15" cy="15" r="8.5" fill="none" stroke="#9c0a12" stroke-width="2" stroke-dasharray="3 1.5"/><path d="M11 15l3 3 5-6" fill="none" stroke="#9c0a12" stroke-width="2"/></svg>
  <svg class="extra-badge" style="left:221px" viewBox="0 0 30 30"><circle cx="15" cy="15" r="14" fill="#fff"/><circle cx="15" cy="15" r="8.5" fill="none" stroke="#9c0a12" stroke-width="2" stroke-dasharray="3 1.5"/><path d="M11 15l3 3 5-6" fill="none" stroke="#9c0a12" stroke-width="2"/></svg>
  <svg class="extra-badge" style="left:369px" viewBox="0 0 30 30"><circle cx="15" cy="15" r="14" fill="#fff"/><circle cx="15" cy="15" r="8.5" fill="none" stroke="#9c0a12" stroke-width="2" stroke-dasharray="3 1.5"/><path d="M11 15l3 3 5-6" fill="none" stroke="#9c0a12" stroke-width="2"/></svg>
  <svg class="extra-badge" style="left:517px" viewBox="0 0 30 30"><circle cx="15" cy="15" r="14" fill="#fff"/><circle cx="15" cy="15" r="8.5" fill="none" stroke="#9c0a12" stroke-width="2" stroke-dasharray="3 1.5"/><path d="M11 15l3 3 5-6" fill="none" stroke="#9c0a12" stroke-width="2"/></svg>
</main>
</body>
</html>
```